Real Estate Listing Signs for standard Yard arms

I need real estate listing signs done, for the standard sized sign to be hung beneath a white yard arm. To match existing logo. Information to be included:
-Logo
-Business name
-Phone number
-Marden Fosk Tundra Circle & Marden Fosk realty logos (smaller print)

Colors to be Red and anywhere in the gray scale between black and white, or a combination of those.

Target Market(s)

Drive by visuals

Industry/Entity Type

Real Estate Agent

Colors

Designer to choose only greyscale colors for use in the design.

Requirements
Must have
• My Logo and business name in same/similar font to whats provided, the MF tundra circle logo (small on bottom or corner somewhere), My phone number, and a decent amount of red coloration on the sign.

```html
<!DOCTYPE html>
<html lang="en">
<head>
<meta charset="utf-8">
<title>Brannock Realty – Yard Sign</title>
<link rel="stylesheet" href="https://fonts.googleapis.com/css2?family=Montserrat:wght@300;400;600;700;900&display=swap">
<style>
  :root {
    --red: #ff0a25;
    --black: #0d0d0d;
    --sign: #e6e6e6;
    --backdrop: #f4f4f4;
    --rule: #9a9a9a;
    --white: #ffffff;
  }
  * { margin: 0; padding: 0; box-sizing: border-box; }
  html, body {
    width: 1200px; height: 1200px; overflow: hidden;
    background: var(--backdrop);
    font-family: "Montserrat", sans-serif;
  }
  .yard-sign {
    position: absolute; left: 180px; top: 40px;
    width: 840px; height: 1120px;
    background: var(--sign);
    box-shadow: 0 4px 18px rgba(0,0,0,0.12);
    display: flex; flex-direction: column; align-items: center;
  }
  .top-band {
    width: 790px; height: 30px; margin-top: 22px;
    background: var(--red);
  }
  .brand-square {
    width: 88px; height: 88px; margin-top: 104px;
    background: var(--red);
  }
  .brand-name {
    margin-top: 34px;
    font-weight: 600; font-size: 44px; letter-spacing: 6px;
    color: var(--black);
  }
  .agent-first {
    margin-top: 18px;
    font-weight: 300; font-size: 104px; letter-spacing: 2px; line-height: 1;
    color: var(--black);
  }
  .agent-last {
    font-weight: 900; font-size: 102px; line-height: 1.02;
    color: var(--black);
  }
  .phone {
    margin-top: 4px;
    display: flex; align-items: center; gap: 16px;
    font-weight: 700; font-size: 72px; color: var(--red);
  }
  .phone svg { width: 56px; height: 56px; }
  .email {
    margin-top: 6px;
    font-weight: 400; font-size: 36px; letter-spacing: 2px;
    color: var(--black);
  }
  .affiliate {
    margin-top: 44px;
    display: flex; align-items: center; gap: 22px;
  }
  .affiliate .rule { width: 210px; height: 2px; background: var(--rule); }
  .affiliate-name {
    font-weight: 600; font-size: 26px; color: #3a3a3a;
    text-align: center; line-height: 1.1;
  }
  .affiliate-sub {
    display: block; font-weight: 600; font-size: 13px; letter-spacing: 2px; color: #3a3a3a;
  }
  .footer-band {
    position: absolute; left: 18px; right: 18px; bottom: 18px; height: 150px;
    background: var(--red);
    display: flex; align-items: center; justify-content: center;
    text-align: center;
    color: var(--white); font-weight: 600; font-size: 40px; letter-spacing: 3px; line-height: 1.1;
  }
</style>
</head>
<body>
  <main class="yard-sign">
    <div class="top-band"></div>
    <div class="brand-square"></div>
    <div class="brand-name">BRANNOCK REALTY</div>
    <div class="agent-first">JORDAN</div>
    <div class="agent-last">BRANNOCK</div>
    <div class="phone">
      <svg viewBox="0 0 56 56" aria-hidden="true">
        <path d="M14 6c2 0 4 5 6 10 1 3-3 5-3 7 2 6 8 12 14 14 2 0 4-4 7-3 5 2 10 4 10 6 0 4-5 10-9 10C22 50 6 34 6 17 6 12 10 6 14 6z" fill="var(--black)"/>
        <path d="M32 16a9 9 0 0 1 8 8M33 8a17 17 0 0 1 15 15M34 0a25 25 0 0 1 22 22" fill="none" stroke="var(--black)" stroke-width="3" stroke-linecap="round"/>
      </svg>
      <span>907-555-0148</span>
    </div>
    <div class="email">jbrannock@mailbox.com</div>
    <div class="affiliate">
      <span class="rule"></span>
      <div class="affiliate-name">MF tundra circle<span class="affiliate-sub">MARDEN FOSK REALTY</span></div>
      <span class="rule"></span>
    </div>
    <div class="footer-band">EACH OFFICE INDEPENDENTLY<br>OWNED AND OPERATED</div>
  </main>
</body>
</html>
```